Women's Online Clothing Boutique Needs Business Cards

I already have a logo that I would like to use. Some of the things that interest me is black business cards, foil embossed logo, glossy embossed logo, leopard print, no yellow font, rounded edges. I even like just a large logo on the front side with all of my information on the back side.

Contact Information for Business Card

https://copperfinch.shopvendly.example/
https://www.facebook.com/thecopperfinchboutique/
https://www.instagram.com/thecopperfinchboutique/
copperfinchboutique@mailora.example

Requirements
Must have
• My Logo
Nice to have
• Leopard Print
Should not have
• No Yellow Font

```html
<!DOCTYPE html>
<html lang="en">
<head>
<meta charset="utf-8">
<title>The Copper Finch Boutique — Business Card</title>
<link rel="stylesheet" href="https://fonts.googleapis.com/css2?family=Roboto:wght@400;500&display=swap">
<style>
  :root {
    --backdrop: #2a2a2a;
    --card: #1e1e1e;
    --gold: #c99a34;
    --gold-soft: #b88a2c;
  }
  * { margin: 0; padding: 0; box-sizing: border-box; }
  html, body {
    width: 1200px;
    height: 901px;
    overflow: hidden;
    background: var(--backdrop);
    font-family: "Roboto", Arial, sans-serif;
  }
  .stage {
    width: 1200px;
    height: 901px;
    display: flex;
    flex-direction: column;
    align-items: center;
    justify-content: center;
    gap: 40px;
  }
  .card {
    width: 640px;
    height: 366px;
    background: var(--card);
    border-radius: 14px;
    position: relative;
    color: var(--gold);
  }
  .card-front {
    display: flex;
    align-items: center;
    justify-content: center;
  }
  .brand-name {
    font-size: 40px;
    font-weight: 500;
    letter-spacing: 0.5px;
    color: var(--gold);
  }
  .card-back {
    display: flex;
    align-items: center;
    justify-content: center;
    gap: 26px;
    padding-left: 40px;
  }
  .person {
    text-align: right;
  }
  .person-name {
    font-size: 26px;
    font-weight: 500;
    line-height: 1.1;
  }
  .person-role {
    font-size: 18px;
    font-weight: 400;
    color: var(--gold-soft);
    margin-top: 2px;
  }
  .divider {
    width: 1.5px;
    height: 108px;
    background: var(--gold);
  }
  .contacts {
    list-style: none;
    display: flex;
    flex-direction: column;
    gap: 6px;
  }
  .contact {
    display: flex;
    align-items: center;
    gap: 10px;
    font-size: 17px;
    font-weight: 400;
    line-height: 1.2;
  }
  .contact-icon {
    width: 15px;
    height: 15px;
    flex: none;
  }
  .contact-icon.plain-mark {
    background: var(--gold);
    border-radius: 3px;
  }
</style>
</head>
<body>
  <main class="stage">
    <section class="card card-front">
      <span class="brand-name">The Copper Finch Boutique</span>
    </section>

    <section class="card card-back">
      <div class="person">
        <div class="person-name">Marianne Hollis</div>
        <div class="person-role">Manager</div>
      </div>
      <div class="divider"></div>
      <ul class="contacts">
        <li class="contact">
          <span class="contact-icon plain-mark"></span>
          <span>thecopperfinchboutique</span>
        </li>
        <li class="contact">
          <span class="contact-icon plain-mark"></span>
          <span>thecopperfinchboutique</span>
        </li>
        <li class="contact">
          <svg class="contact-icon" viewBox="0 0 16 16" aria-hidden="true">
            <rect x="1" y="3" width="14" height="10" rx="1" fill="none" stroke="currentColor" stroke-width="1.4"/>
            <path d="M1.5 3.8 L8 9 L14.5 3.8" fill="none" stroke="currentColor" stroke-width="1.4"/>
          </svg>
          <span>copperfinchboutique@mailora.example</span>
        </li>
        <li class="contact">
          <svg class="contact-icon" viewBox="0 0 16 16" aria-hidden="true">
            <circle cx="8" cy="8" r="6.8" fill="none" stroke="currentColor" stroke-width="1.3"/>
            <ellipse cx="8" cy="8" rx="3" ry="6.8" fill="none" stroke="currentColor" stroke-width="1.1"/>
            <path d="M1.2 8 H14.8 M2.4 4.6 H13.6 M2.4 11.4 H13.6" fill="none" stroke="currentColor" stroke-width="1.1"/>
          </svg>
          <span>copperfinch.shopvendly.example</span>
        </li>
      </ul>
    </section>
  </main>
</body>
</html>
```